Business Card Design

We are looking for a business card designed for our landscaping company. We do landscaping installation & Maintenance Services. We would like to see designs that have basic landscaping in background. We also think it is important to have both of our names and phone numbers on the card. We need something that stands out a little whether it is shape of the card or thickness or design.

Industry/Entity Type

Business

Contact Information for Business Card

Pale Ridge Yardworks, paleridgeyardworks@mailbrook.net, Dale Purvine 555-213-7690, Martin Kolbey 555-864-1037

```html
<!DOCTYPE html>
<html lang="en">
<head>
<meta charset="utf-8">
<title>Pale Ridge Yardworks – Business Cards</title>
<link href="https://fonts.googleapis.com/css2?family=Ubuntu:wght@400;500;700&display=swap" rel="stylesheet">
<style>
  :root{
    --bg:#e6e8ea;
    --card:#ffffff;
    --ink:#3a3d42;
    --muted:#8a8d92;
    --accent:#1fa9ea;
    --band-top:#050505;
    --band-bottom:#2a2a2a;
    --base-gray:#d9dadc;
    --map-tone:#f1f2f4;
    --sky:#2d4fd6;
    --sky-deep:#1a2a9c;
    --lawn:#3f8f4a;
    --lawn-light:#7cc25a;
  }
  *{box-sizing:border-box;margin:0;padding:0}
  html,body{width:1200px;height:1000px;overflow:hidden}
  body{
    background:var(--bg);
    font-family:"Ubuntu",sans-serif;
    display:flex;flex-direction:column;align-items:center;justify-content:center;gap:60px;
  }
  .card{
    position:relative;width:700px;height:400px;border-radius:26px;overflow:hidden;
    background:var(--card);box-shadow:0 10px 28px rgba(0,0,0,.18);
  }
  .card__shapes{position:absolute;inset:0}
  .card__tagline{
    position:absolute;left:44px;top:52px;font-size:15px;letter-spacing:.5px;color:var(--muted);
    text-transform:uppercase;
  }
  .card__contact{position:absolute;top:114px}
  .card__contact--first{left:44px}
  .card__contact--second{left:262px}
  .card__name{font-size:24px;font-weight:500;color:var(--accent);line-height:30px;white-space:nowrap}
  .card__phone{font-size:16px;color:#fff;letter-spacing:.5px;line-height:24px;margin-top:4px}
  .card__company{
    position:absolute;left:44px;top:248px;font-size:24px;line-height:28px;font-weight:700;color:var(--ink);
    text-transform:uppercase;letter-spacing:.5px;
  }
  .card__email{
    position:absolute;left:44px;top:334px;font-size:17px;color:var(--ink);
  }
</style>
</head>
<body>

  <article class="card">
    <svg class="card__shapes" viewBox="0 0 700 400" width="700" height="400">
      <defs>
        <linearGradient id="bandFill" x1="0" y1="0" x2="0" y2="1">
          <stop offset="0" stop-color="var(--band-top)"/>
          <stop offset="1" stop-color="var(--band-bottom)"/>
        </linearGradient>
        <linearGradient id="sceneFill" x1="0" y1="0" x2="0" y2="1">
          <stop offset="0" stop-color="var(--sky)"/>
          <stop offset=".45" stop-color="var(--sky-deep)"/>
          <stop offset=".6" stop-color="var(--lawn)"/>
          <stop offset="1" stop-color="var(--lawn-light)"/>
        </linearGradient>
      </defs>
      <rect class="map-area" x="0" y="230" width="400" height="170" fill="var(--map-tone)" role="img" aria-label="Faint dotted map texture in the background"/>
      <polygon class="base-stripe" points="0,190 490,190 470,230 0,230" fill="var(--base-gray)"/>
      <polygon class="image-panel" points="450,0 700,0 700,400 350,400" fill="url(#sceneFill)" role="img" aria-label="Photo of a landscaped yard with lawn, shrubs and blue sky"/>
      <polygon class="name-band" points="0,95 520,95 485,190 0,190" fill="url(#bandFill)"/>
    </svg>
    <p class="card__tagline">Installation &amp; Maintenance Services</p>
    <div class="card__contact card__contact--first">
      <h2 class="card__name">Dale Purvine</h2>
      <p class="card__phone">555 213 7690</p>
    </div>
    <div class="card__contact card__contact--second">
      <h2 class="card__name">Martin Kolbey</h2>
      <p class="card__phone">555 864 1037</p>
    </div>
    <p class="card__company">Pale Ridge<br>Yardworks</p>
    <p class="card__email">paleridgeyardworks@mailbrook.net</p>
  </article>

  <article class="card">
    <svg class="card__shapes" viewBox="0 0 700 400" width="700" height="400">
      <defs>
        <linearGradient id="bandFill2" x1="0" y1="0" x2="0" y2="1">
          <stop offset="0" stop-color="var(--band-top)"/>
          <stop offset="1" stop-color="var(--band-bottom)"/>
        </linearGradient>
        <linearGradient id="sceneFill2" x1="0" y1="0" x2="0" y2="1">
          <stop offset="0" stop-color="var(--sky)"/>
          <stop offset=".45" stop-color="var(--sky-deep)"/>
          <stop offset=".6" stop-color="var(--lawn)"/>
          <stop offset="1" stop-color="var(--lawn-light)"/>
        </linearGradient>
      </defs>
      <rect class="map-area" x="0" y="230" width="400" height="170" fill="var(--map-tone)" role="img" aria-label="Faint dotted map texture in the background"/>
      <polygon class="base-stripe" points="0,190 490,190 470,230 0,230" fill="var(--base-gray)"/>
      <polygon class="image-panel" points="450,0 700,0 700,400 350,400" fill="url(#sceneFill2)" role="img" aria-label="Photo of a landscaped yard with lawn, shrubs and blue sky"/>
      <polygon class="name-band" points="0,95 520,95 485,190 0,190" fill="url(#bandFill2)"/>
    </svg>
    <p class="card__tagline">Installation &amp; Maintenance Services</p>
    <div class="card__contact card__contact--first">
      <h2 class="card__name">Martin Kolbey</h2>
      <p class="card__phone">555 864 1037</p>
    </div>
    <div class="card__contact card__contact--second">
      <h2 class="card__name">Dale Purvine</h2>
      <p class="card__phone">555 213 7690</p>
    </div>
    <p class="card__company">Pale Ridge<br>Yardworks</p>
    <p class="card__email">paleridgeyardworks@mailbrook.net</p>
  </article>

</body>
</html>
```